Podcast Marketing Template for LinkedIn

I would like to have graphics to post notices of new podcast episodes on LinkedIn as release new episodes.
The graphics need to be in a template form that can be easily updated by my VA.
Each episode will have a new title and guest.
Two examples of a ROUGH DRAFT of an episode example are attached.
(I do not like these because I think they reflect the standards I have for my brand.)
The posts should be bright and clean and clearly reflect QUALITY of the podcast in the quality of the design. Audience and interviewees are CEOs.
Please refer to my website and podcast art to see brand direction.
www.lorenbriskadvisory.com
Each

```html
<!DOCTYPE html>
<html lang="en">
<head>
<meta charset="utf-8">
<title>Steady Summit Podcast – Episode Graphics</title>
<link href="https://fonts.googleapis.com/css2?family=Poppins:wght@300;400;600;700&display=swap" rel="stylesheet">
<style>
  :root{
    --board:#e2e2e2;
    --ink:#0a0c10;
    --ink-soft:#1a1f27;
    --brand-blue:#1b5fae;
    --brand-deep:#0a2c63;
    --accent:#3d9be9;
    --white:#ffffff;
    --photo-light:#cfcfcf;
    --photo-dark:#3a3a3a;
  }
  *{box-sizing:border-box;margin:0;padding:0}
  html,body{width:943px;height:1200px;overflow:hidden;background:var(--board);font-family:'Poppins',sans-serif}
  .board{position:relative;width:943px;height:1200px}
  .post{position:absolute;overflow:hidden;background:radial-gradient(circle at 70% 40%,var(--ink-soft) 0%,var(--ink) 70%);box-shadow:0 6px 14px rgba(0,0,0,.35);color:var(--white)}
  .post > *{z-index:2}
  .post--square{left:223px;top:106px;width:496px;height:496px}
  .post--wide{left:89px;top:676px;width:764px;height:428px}
  .host-panel{position:absolute;top:0;right:0;height:100%;z-index:0 !important;background:linear-gradient(160deg,var(--brand-blue) 0%,#124a92 45%,var(--brand-deep) 100%)}
  .post--square .host-panel{width:178px}
  .post--wide .host-panel{width:197px}
  .show-mark{position:absolute;background:linear-gradient(180deg,#e8edf3,#8ea3bd)}
  .show-name{position:absolute;font-weight:700;line-height:1.02}
  .title-light{position:absolute;font-weight:300;line-height:1;white-space:nowrap}
  .title-bold{position:absolute;font-weight:700;line-height:1;white-space:nowrap}
  .amp{position:absolute;border-radius:50%;background:var(--brand-blue);font-weight:700;display:flex;align-items:center;justify-content:center}
  .subtitle{position:absolute;color:var(--accent);font-weight:600;white-space:nowrap;line-height:1}
  .rule{position:absolute;height:2px;background:#3a3f47}
  .guest-photo{position:absolute;bottom:0;z-index:1 !important;background:linear-gradient(180deg,var(--photo-dark) 0%,var(--photo-light) 45%,#e8e8e8 70%,#2a2a2a 100%)}
  .post--square .guest-photo{clip-path:polygon(18% 8%,28% 0,52% 0,61% 10%,60% 48%,85% 60%,100% 100%,0 100%,0 58%,18% 50%)}
  .post--wide .guest-photo{clip-path:polygon(44% 6%,55% 0,82% 0,93% 10%,93% 50%,100% 56%,100% 100%,0 100%,10% 66%,44% 55%)}
  .with{position:absolute;font-weight:600;line-height:1}
  .person-name{position:absolute;font-weight:700;line-height:1;text-transform:uppercase;white-space:nowrap}
  .person-role{position:absolute;color:var(--accent);font-weight:600;text-transform:uppercase;white-space:nowrap;line-height:1}
  .host-photo{position:absolute;border-radius:50%;background:radial-gradient(circle at 50% 40%,#ffffff 0%,#d6d6d6 55%,#555 100%);border:5px solid #2b6cb8}
  .podcast-label{position:absolute;font-weight:400;letter-spacing:6px;line-height:1}
</style>
</head>
<body>
<div class="board">

  <section class="post post--square">
    <div class="host-panel" role="img" aria-label="Blue-tinted photo of a glass office tower"></div>
    <div class="show-mark" style="left:36px;top:41px;width:55px;height:55px"></div>
    <div class="show-name" style="left:99px;top:38px;font-size:21px">Steady<br>Summit<br>Podcast</div>

    <div class="title-light" style="left:36px;top:129px;font-size:40px">Technology</div>
    <div class="amp" style="left:271px;top:133px;width:34px;height:34px;font-size:22px">&amp;</div>
    <div class="title-bold" style="left:35px;top:170px;font-size:39px">Philanthropy</div>
    <div class="subtitle" style="left:36px;top:216px;font-size:19px;letter-spacing:5px">IN EDUCATION</div>

    <div class="guest-photo" role="img" aria-label="Black and white portrait of the guest" style="left:0;width:246px;height:251px"></div>
    <div class="with" style="left:168px;top:297px;font-size:13px">with</div>
    <div class="person-name" style="left:168px;top:315px;font-size:24px">Ilan<br>Voss</div>
    <div class="person-role" style="left:168px;top:368px;font-size:11.5px;letter-spacing:2.5px">CEO of Wrenly</div>

    <div class="host-photo" role="img" aria-label="Portrait of the host" style="left:342px;top:176px;width:126px;height:126px"></div>
    <div class="person-name" style="left:351px;top:315px;font-size:24px">Loren<br>Brisk</div>
    <div class="person-role" style="left:351px;top:368px;font-size:11.5px;letter-spacing:2.5px">Host</div>
    <div class="podcast-label" style="left:347px;top:449px;font-size:17px">PODCAST</div>
  </section>

  <section class="post post--wide">
    <div class="host-panel" role="img" aria-label="Blue-tinted photo of a glass office tower"></div>
    <div class="guest-photo" role="img" aria-label="Black and white portrait of the guest" style="left:256px;width:311px;height:364px"></div>

    <div class="show-mark" style="left:44px;top:47px;width:72px;height:72px"></div>
    <div class="show-name" style="left:126px;top:43px;font-size:27px">Steady<br>Summit<br>Podcast</div>

    <div class="title-light" style="left:45px;top:157px;font-size:46px">Technology</div>
    <div class="amp" style="left:318px;top:159px;width:44px;height:44px;font-size:28px">&amp;</div>
    <div class="title-bold" style="left:43px;top:205px;font-size:45px">Philanthropy</div>
    <div class="subtitle" style="left:43px;top:256px;font-size:21px;letter-spacing:6px">IN EDUCATION</div>
    <div class="rule" style="left:43px;top:290px;width:55px"></div>

    <div class="with" style="left:44px;top:324px;font-size:16px">with</div>
    <div class="person-name" style="left:43px;top:344px;font-size:31px">Ilan Voss</div>
    <div class="person-role" style="left:43px;top:379px;font-size:15px;letter-spacing:3.5px">CEO of Wrenly</div>

    <div class="host-photo" role="img" aria-label="Portrait of the host" style="left:600px;top:167px;width:132px;height:132px"></div>
    <div class="person-name" style="left:607px;top:326px;font-size:27px">Loren<br>Brisk</div>
    <div class="person-role" style="left:607px;top:381px;font-size:14px;letter-spacing:3px">Host</div>
  </section>

</div>
</body>
</html>
```